Qorby Labs

I am a CBD Manufacturer I would have a site more laid out in a lab format
current site is qorbylabs.example what Id like is a site like tarnwellabs.example

Target Market(s)

Any one needing cbd oil and finished goods

Coding

Coded - Design and coding required

Number of Pages Required

1 page

```html
<!DOCTYPE html>
<html lang="en">
<head>
<meta charset="utf-8">
<title>Qorby Labs</title>
<link rel="stylesheet" href="https://fonts.googleapis.com/css2?family=Poppins:wght@300;400;500;600;700;800&display=swap">
<style>
:root{
  --yellow:#fdd96f;
  --ink:#161616;
  --text:#2a2a2a;
  --gold:#caa140;
  --stage:#6e6e6e;
  --panel:#f2f2f2;
  --footer:#333333;
  --white:#ffffff;
}
*{box-sizing:border-box;margin:0;padding:0}
html,body{width:1200px;height:4000px;overflow:hidden;background:var(--stage);font-family:'Poppins',sans-serif;color:var(--text)}
.page{position:absolute;left:73px;top:20px;width:1053px;height:3960px;background:var(--white);overflow:hidden}
.abs{position:absolute}
/* top bar */
.topbar{left:0;top:0;width:1053px;height:58px;background:var(--yellow);font-size:7px;color:var(--ink)}
.topbar .info{top:24px;display:flex;align-items:center;gap:5px;white-space:nowrap}
.topbar svg{width:10px;height:10px}
.pill{height:29px;border:2px solid var(--ink);border-radius:15px;display:flex;align-items:center;justify-content:center;font-size:12px;color:var(--ink)}
/* nav */
.brand{left:125px;top:74px;font-size:34px;font-weight:300;color:var(--gold);letter-spacing:1px}
.nav a{position:absolute;top:92px;font-size:15px;color:var(--ink);text-decoration:none}
/* hero */
.hero{left:0;top:139px;width:1053px;height:592px}
.hero h1{position:absolute;left:613px;top:140px;font-size:54px;line-height:64px;font-weight:800;color:var(--ink);letter-spacing:-0.5px}
.hero p{position:absolute;left:618px;font-size:16px;line-height:20px;color:var(--ink);width:360px}
.btn-outline{position:absolute;left:632px;top:384px;width:168px;height:46px;border:2px solid var(--ink);border-radius:23px;display:flex;align-items:center;justify-content:center;font-size:17px;color:var(--ink)}
.badge{top:744px;width:72px;height:72px;border-radius:50%;background:#3d8f3a;border:4px solid #dfeedd}
/* benefits */
.benefits{left:0;top:854px;width:1053px;height:487px}
.benefits h2{position:absolute;left:37px;top:70px;font-size:27px;line-height:33px;font-weight:700;color:var(--ink)}
.benefit{position:absolute;left:37px;display:flex;gap:8px;font-size:16px;line-height:20px;color:var(--ink);width:390px}
.benefit svg{flex:0 0 24px;height:24px;margin-top:-2px}
/* products */
.products{left:0;top:1341px;width:1053px;height:1091px;background:var(--panel)}
.card{position:absolute;background:var(--white);box-shadow:0 1px 3px rgba(0,0,0,.08)}
.card h3{position:absolute;top:182px;font-size:34px;font-weight:700;color:var(--ink);line-height:40px}
.card p{position:absolute;top:222px;font-size:17px;line-height:22px;color:var(--ink)}
.shop{position:absolute;top:373px;width:138px;height:38px;border-radius:19px;background:var(--yellow);font-size:13px;display:flex;align-items:center;justify-content:center;color:var(--ink)}
.ph{position:absolute}
/* welcome */
.welcome{left:0;top:2432px;width:1053px;height:488px;background:linear-gradient(120deg,#1d4a76 0%,#4e7ca8 45%,#2d5a86 75%,#8a8a52 100%);text-align:center;color:var(--white)}
.welcome h2{position:absolute;left:0;width:100%;top:118px;font-size:34px;font-weight:800}
.welcome p{position:absolute;left:165px;width:723px;top:164px;font-size:24px;line-height:30px;font-weight:400}
.btn-fill{position:absolute;left:459px;top:320px;width:136px;height:38px;border-radius:19px;background:var(--yellow);color:var(--ink);font-size:13px;display:flex;align-items:center;justify-content:center}
/* knowledge */
.knowledge{left:0;top:2976px;width:1053px;height:488px}
.knowledge h2{position:absolute;left:605px;top:62px;font-size:28px;font-weight:700;color:var(--ink)}
.qa{position:absolute;left:605px;width:400px;font-size:15px;line-height:19px;color:var(--ink)}
.qa b{display:inline-block;background:var(--yellow);font-size:14px;font-weight:700;padding:0 3px;line-height:17px;margin-bottom:1px}
/* notify */
.notify h2{position:absolute;left:0;width:1053px;text-align:center;top:3526px;font-size:26px;font-weight:500;color:var(--ink)}
.notify small{position:absolute;left:0;width:1053px;text-align:center;top:3568px;font-size:9px;color:var(--ink)}
.field{left:322px;top:3600px;width:300px;height:35px;background:#f3f3f3;border-radius:18px 0 0 18px;font-size:9px;color:#999;padding:12px 16px}
.notify-btn{left:611px;top:3600px;width:122px;height:35px;background:var(--yellow);border-radius:18px;font-size:9px;color:var(--white);display:flex;align-items:center;justify-content:center}
/* footer */
.footer{left:0;top:3723px;width:1053px;height:237px;background:var(--footer);color:var(--white)}
.footer h4{position:absolute;top:26px;font-size:17px;font-weight:500;color:var(--yellow)}
.footer .col{position:absolute;top:88px;font-size:10px;line-height:13px}
.footer .links a{display:block;color:var(--white);text-decoration:none;line-height:14px;margin-bottom:14px;font-size:10px}
</style>
</head>
<body>
<div class="page">

  <header class="abs topbar">
    <div class="abs info" style="left:101px"><svg viewBox="0 0 10 10"><path d="M1 6v-1a4 4 0 0 1 8 0v1M1 6h2v3H1zM7 6h2v3H7z" fill="none" stroke="#161616"/></svg>+1 555 014 2284</div>
    <div class="abs info" style="left:190px"><svg viewBox="0 0 10 10"><rect x="1" y="2" width="8" height="6" fill="none" stroke="#161616"/><path d="M1 2l4 3 4-3" fill="none" stroke="#161616"/></svg>noreply@qorbylabs.example</div>
    <div class="abs info" style="left:338px">Mon - Sat 8:00 - 18:00, Sunday</div>
    <svg class="abs" style="left:640px;top:20px" width="14" height="14" viewBox="0 0 14 14"><circle cx="7" cy="4.5" r="3" fill="none" stroke="#161616"/><path d="M2 13a5 5 0 0 1 10 0" fill="none" stroke="#161616"/></svg>
    <svg class="abs" style="left:678px;top:20px" width="20" height="14" viewBox="0 0 20 14"><path d="M1 2h3l2 7h8l2-5H5" fill="none" stroke="#161616"/><circle cx="16" cy="4" r="3.5" fill="#e04040"/></svg>
    <div class="abs pill" style="left:707px;top:14px;width:111px">Sign Up</div>
    <div class="abs pill" style="left:824px;top:14px;width:109px">Login</div>
  </header>

  <div class="abs brand">Qorby Labs</div>
  <nav class="nav">
    <a style="left:381px">Home</a><a style="left:480px">Community</a><a style="left:618px">Shop</a><a style="left:677px">Wholesale</a><a style="left:776px">Contact</a>
  </nav>

  <section class="abs hero">
    <svg class="abs" style="left:0;top:0" width="1053" height="592"><polygon points="456,0 1053,0 1053,592 656,592" fill="#fdd96f"/></svg>
    <div class="ph" role="img" aria-label="Group of blue glass dropper bottles of CBD oil" style="left:50px;top:109px;width:451px;height:344px;border-radius:14px;background:linear-gradient(160deg,#3a2f8a,#20206a 55%,#c9a84a)"></div>
    <h1>ROLLING ON<br>TO THE SCENE</h1>
    <p style="top:276px">We are proud to serve our community.</p>
    <p style="top:316px">Learn more about what we are doing to help those in need.</p>
    <div class="btn-outline">Learn More</div>
  </section>

  <div class="abs badge" style="left:374px"></div>
  <div class="abs badge" style="left:455px"></div>
  <div class="abs badge" style="left:534px"></div>
  <div class="abs badge" style="left:617px;background:#334a80"></div>

  <section class="abs benefits">
    <svg class="abs" style="left:0;top:0" width="1053" height="487">
      <defs><linearGradient id="labg" x1="0" y1="0" x2="1" y2="1"><stop offset="0" stop-color="#dfe4ea"/><stop offset=".5" stop-color="#f3f1ec"/><stop offset="1" stop-color="#9aa6b2"/></linearGradient></defs>
      <polygon points="556,0 1053,0 1053,487 424,487" fill="url(#labg)" role="img" aria-label="Gloved hand holding a vial of golden CBD oil beside a microscope"/>
      <line x1="556" y1="0" x2="418" y2="487" stroke="#fdd96f" stroke-width="6"/>
    </svg>
    <h2>DISCOVER THE BENEFITS OF<br>QORBY LABS CBD</h2>
    <div class="benefit" style="top:166px"><svg viewBox="0 0 24 24"><circle cx="11" cy="13" r="9" fill="none" stroke="#fdd96f" stroke-width="1.6"/><path d="M6 13l4 4 11-12" fill="none" stroke="#fdd96f" stroke-width="2"/></svg><span>All of our products are tested to ensure the best quality CBD available</span></div>
    <div class="benefit" style="top:228px"><svg viewBox="0 0 24 24"><circle cx="11" cy="13" r="9" fill="none" stroke="#fdd96f" stroke-width="1.6"/><path d="M6 13l4 4 11-12" fill="none" stroke="#fdd96f" stroke-width="2"/></svg><span>Choose from a wide variety of products and flavors including concentrate, edible, tincture, vape pen, body cream, salve, and ointment</span></div>
    <div class="benefit" style="top:330px"><svg viewBox="0 0 24 24"><circle cx="11" cy="13" r="9" fill="none" stroke="#fdd96f" stroke-width="1.6"/><path d="M6 13l4 4 11-12" fill="none" stroke="#fdd96f" stroke-width="2"/></svg><span>We use CO2 extraction and a chemi-cal-free extraction process that is environ-mentally friendly and safe for all of our hemp CBD oil</span></div>
  </section>

  <section class="abs products">
    <div class="card" style="left:43px;top:43px;width:469px;height:480px">
      <div class="ph" role="img" aria-label="Black bottle of CBD lotion" style="left:28px;top:52px;width:160px;height:380px;border-radius:24px;background:linear-gradient(90deg,#0f0f0f,#3a3a3a,#111)"></div>
      <h3 style="left:208px">Lotion</h3><p style="left:204px">Product Description<br>Goes Here</p>
      <div class="shop" style="left:208px">SHOP NOW</div>
    </div>
    <div class="card" style="left:534px;top:43px;width:471px;height:480px">
      <h3 style="left:34px">Roll On Ointment</h3><p style="left:32px">Product Description<br>Goes Here</p>
      <div class="shop" style="left:34px">SHOP NOW</div>
      <div class="ph" role="img" aria-label="Blue roll-on ointment tube" style="left:344px;top:66px;width:78px;height:360px;border-radius:10px;background:linear-gradient(180deg,#111 0 25%,#1e2f9a 25%,#2a3bb8)"></div>
    </div>
    <div class="card" style="left:43px;top:547px;width:469px;height:478px">
      <div class="ph" role="img" aria-label="Vape cartridge in retail blister pack" style="left:34px;top:173px;width:157px;height:256px;border-radius:8px;background:linear-gradient(160deg,#f4f4f4,#d9d9d9)"></div>
      <h3 style="left:211px">Vape Pen</h3><p style="left:209px">Product Description<br>Goes Here</p>
      <div class="shop" style="left:211px;top:373px">SHOP NOW</div>
    </div>
    <div class="card" style="left:534px;top:547px;width:471px;height:478px">
      <h3 style="left:34px">Vape Pen</h3><p style="left:32px">Product Description<br>Goes Here</p>
      <div class="shop" style="left:34px;top:373px">SHOP NOW</div>
      <div class="ph" role="img" aria-label="Round tin of CBD salve" style="left:202px;top:186px;width:243px;height:243px;border-radius:50%;background:radial-gradient(circle at 40% 40%,#7f9aa8,#3f5461 70%,#222)"></div>
    </div>
  </section>

  <section class="abs welcome" role="img" aria-label="Blue-toned laboratory glassware with a dropper releasing oil">
    <h2>WELCOME NEW CUSTOMERS!</h2>
    <p>Lorem ipsum dolor sit amet, consectetur adipiscing elit, sed do eiusmod tempor incididunt ut labore et dolore magna aliqua. Quis ipsum suspendisse ultrices gravida. Risus commodo viverra maecenas accumsan lacus vel facilisis.</p>
    <div class="btn-fill">learn more</div>
  </section>

  <section class="abs knowledge">
    <svg class="abs" style="left:0;top:0" width="1053" height="488">
      <defs><linearGradient id="labk" x1="0" y1="0" x2="1" y2="1"><stop offset="0" stop-color="#e8edf3"/><stop offset=".55" stop-color="#4a86c8"/><stop offset="1" stop-color="#c9c08a"/></linearGradient></defs>
      <polygon points="0,0 594,0 461,488 0,488" fill="url(#labk)" role="img" aria-label="Scientist in blue gloves examining a test tube with a plant sample"/>
      <line x1="596" y1="0" x2="463" y2="488" stroke="#fdd96f" stroke-width="5"/>
    </svg>
    <h2>KNOWLEDGE IS POWER</h2>
    <div class="qa" style="top:106px"><b>WHAT IS CBD?</b><br>Cannabidiol also known as CBD, is a phytocan-nabinoid found in agricultural hemp. Unlike its cousin tetrahydrocannabinol also known as THC, CBD is non-psychotoxic, which means it does not produce feelings of euphoria.</div>
    <div class="qa" style="top:240px"><b>IS IT LEGAL?</b><br>Because all of our CBD products are derived from agricultural hemp and compliant, it is not unlawful to ship across the United States.</div>
    <div class="qa" style="top:336px"><b>IS IT SAFE?</b><br>CBD has a remarkable safety profile and Qorby Labs goes beyond to ensure high quality, safety, and efficacy of our CBD products. All Qorby Labs products are derived from agricultural hemp, are non-psychotoxic, and are produced with care.</div>
  </section>

  <div class="notify">
    <h2>Be Notified</h2>
    <small>Enter you email address to be notified of the launch</small>
    <div class="abs field">Your Mail</div>
    <div class="abs notify-btn">Notify</div>
  </div>

  <footer class="abs footer">
    <h4 style="left:270px">QUICK LINKS</h4>
    <h4 style="left:446px">NOTICE</h4>
    <h4 style="left:653px">ABOUT US</h4>
    <div class="col links" style="left:270px;top:88px"><a>Mission</a><a>Customer Satisfaction</a><a>Shipping &amp; Return Policy</a><a style="margin-top:6px">Privacy Policy</a><a>Terms of Service</a></div>
    <div class="col" style="left:446px;width:170px">The statements regarding these products have not been evaluated by the Food and Drug Administration. These products are not intended to diagnose, treat, cure or prevent any disease. Results from products may vary.</div>
    <div class="col" style="left:653px;width:165px">Qorby Labs prides itself on delivering our customers the highest quality full spectrum CBD infused products. Our products are made using the finest-quality, natural ingredients, and contain only 100% hemp sourced in the U.S.</div>
  </footer>

</div>
</body>
</html>
```